Solo consultant in research/analytics/data science space needs new business card

I need a new business card to promote my solo business as creative problem solver and consultant. I work on business projects for sales and market research and analytics, customer/market insights, and data science. I provide clients data-informed insights and ideas to enhance their businesses. My initial tagline: 'Make your data work for YOU.'

People should hire me because of my diverse background. Because of my Ph.D. in Political Science I have a strong background in research and analytics, project design and management, and communications skills. With my experience as a marketing analyst, a volunteer on non-profit projects, and currently as research consultant I have worked on projects within various industries. I also have a taste for improvisation so I enjoy thinking creatively and appreciate design thinking.

As an introduction to my background: Clients might want to hire me for many types of projects. Clients might wish to understand who their best customers are and how to characterize them. Maybe clients want to know how their customers feel about a certain product or service. Clients might want to know more about their local market area and overall industry. Clients might want to know whether their marketing programs are effective or else what drives their sales revenue. Perhaps clients want to use their data to create something useful for themselves or their customers.

One client hired me to help them decide whether to expand their services to newer customers. I gathered and analyzed information about the local area – the characteristics of people living there as well as the client’s competitors – and described trends and implications. The client was very pleased with the results and submitted them to superiors for approval to move forward.

For another client – who was looking to purchase a house in a metropolitan area – I gathered population and school data about the area. With this, I created an interactive mapping tool so they could zoom in on neighborhoods and learn more about them before they selected a neighborhood to purchase a house. They were happy with the results of my work.

When I worked as a marketing analyst for a consulting firm, a Vice President of Marketing hired us to discover whether or not the company’s marketing programs (i.e. coupons and discounts) were effective. I analyzed their data and our team discovered their marketing was indeed effective. He was very happy and used this to justify their programs to the Finance department (who thought such programs lost revenue).

- Mark Dennis Hollow, Ph.D.

Target Market(s)

Future clients and employers. The most immediate target markets will be other service providers such as consulting companies, marketing firms and ad agencies. I will also use this for meeting with clients in various industries.

Industry/Entity Type

Consulting

Contact Information for Business Card

Since it is my first real business card as a solo practitioner, I want to make an excellent first impression. I want this useful in case someone hires me to work on projects or else hire me to work within a firm or company. The card should convey competence and some creativity while also being neither stuffy nor a data geek.

Colors

Designer to choose colors to be used in the design.

Requirements
Nice to have
• Attached are the starting efforts at the card to add some color. It will be nice to use my name and descriptors on one side and tagline on the other. If anyone has better ideas, I will love to see them!

```html
<!DOCTYPE html>
<html lang="en">
<head>
<meta charset="utf-8">
<title>Mark Dennis Hollow — Business Card</title>
<link rel="stylesheet" href="https://fonts.googleapis.com/css2?family=Lato:wght@400;700&family=Crimson+Text:ital@1&display=swap">
<style>
  :root {
    --backdrop: #d9d9d6;
    --card: #161616;
    --ink: #f2f2f2;
    --accent: #e0573f;
    --ghost: #232323;
  }
  * { box-sizing: border-box; margin: 0; padding: 0; }
  html, body { width: 1200px; height: 824px; overflow: hidden; }
  body {
    background: var(--backdrop);
    font-family: "Lato", sans-serif;
    color: var(--ink);
    position: relative;
  }
  .card {
    position: absolute;
    top: 258px;
    width: 540px;
    height: 309px;
    background: var(--card);
    border-radius: 4px;
    box-shadow: 0 10px 28px rgba(0,0,0,.25);
    overflow: hidden;
  }
  .card--back { left: 40px; }
  .card--front { left: 620px; }

  /* back: tagline */
  .tagline-block {
    position: absolute; inset: 0;
    display: flex; flex-direction: column; align-items: center; justify-content: center;
  }
  .brand-ghost {
    position: absolute; left: 50%; top: 50%;
    transform: translate(-50%, -50%);
    font-size: 64px; font-weight: 400; white-space: nowrap;
    color: var(--ghost);
  }
  .rule-short { width: 60px; height: 1.5px; background: var(--accent); position: relative; }
  .tagline {
    position: relative;
    font-size: 34px; line-height: 1.05; font-weight: 400; text-align: left;
    margin: 20px 0;
  }

  /* front: identity */
  .brand-name {
    position: absolute; right: 40px; top: 50px;
    font-size: 30px; font-weight: 400; white-space: nowrap;
    color: var(--accent);
  }
  .identity { position: absolute; left: 36px; top: 112px; }
  .name { font-size: 19px; font-weight: 400; letter-spacing: .3px; text-transform: uppercase; }
  .name small { font-size: 14px; }
  .role {
    font-family: "Crimson Text", serif; font-style: italic;
    font-size: 14px; line-height: 1.1; color: var(--accent); margin-top: 3px;
  }
  .divider { position: absolute; left: 36px; right: 36px; top: 178px; height: 1px; background: var(--accent); }
  .contact-list { position: absolute; left: 36px; top: 192px; list-style: none; font-size: 14px; line-height: 1.7; }
  .contact-list li, .social-list li { display: flex; align-items: center; gap: 9px; }
  .social-list { position: absolute; right: 36px; bottom: 22px; list-style: none; font-size: 15px; line-height: 1.7; }
  .social-list li { justify-content: flex-end; }
  .icon { width: 12px; height: 12px; flex: none; }
  .icon-square { width: 12px; height: 12px; border-radius: 2px; background: var(--accent); flex: none; }
</style>
</head>
<body>
  <section class="card card--back" aria-label="Card back">
    <div class="tagline-block">
      <span class="brand-ghost">M.D. Hollow</span>
      <span class="rule-short"></span>
      <p class="tagline">Make your data<br>work for YOU.</p>
      <span class="rule-short"></span>
    </div>
  </section>

  <section class="card card--front" aria-label="Card front">
    <span class="brand-name">M.D. Hollow</span>
    <div class="identity">
      <h1 class="name">Mark Dennis Hollow, <small>Ph.D.</small></h1>
      <p class="role">Reasearch/Analytics - Customer Intelligence - Date Science<br>Consultant</p>
    </div>
    <div class="divider"></div>
    <ul class="contact-list">
      <li>
        <svg class="icon" viewBox="0 0 12 12"><path d="M6 0.5a4 4 0 0 0-4 4c0 3 4 7 4 7s4-4 4-7a4 4 0 0 0-4-4z" fill="var(--accent)"/><circle cx="6" cy="4.5" r="1.4" fill="var(--card)"/></svg>
        Lisbon, PT
      </li>
      <li>
        <svg class="icon" viewBox="0 0 12 12"><path d="M2.5 1l2 .3.8 2.4-1.2 1a6.5 6.5 0 0 0 3.2 3.2l1-1.2 2.4.8.3 2-1.5 1.5C5 10.5 1.5 7 1 2.5z" fill="var(--accent)"/></svg>
        +351 912 345 678
      </li>
      <li>
        <svg class="icon" viewBox="0 0 12 12"><rect x="0.5" y="2" width="11" height="8" fill="var(--accent)"/><path d="M0.5 2l5.5 4.5L11.5 2" fill="none" stroke="var(--card)" stroke-width="1"/></svg>
        mdhollow70@inboxmail.com
      </li>
    </ul>
    <ul class="social-list">
      <li>@markHollow70 <span class="icon-square"></span></li>
      <li>markdennishollow.com
        <svg class="icon" viewBox="0 0 12 12" fill="none" stroke="var(--accent)" stroke-width="1.1"><circle cx="6" cy="6" r="5"/><ellipse cx="6" cy="6" rx="2.2" ry="5"/><path d="M1 6h10"/></svg>
      </li>
    </ul>
  </section>
</body>
</html>
```